Surface Protection company needs cards

We are a New Zealand company that will apply nanotechnology coatings on surfaces to prevent growth and spread of bacteria, viruses, mold etc with a sprayer. We deal with large corporates, airlines, hospitals and schools so we are after a new modern, simple and clean look that will have great visual impact.
We a company that is focused on prevention and protection.

Company name, Vela Shield

Subtext, Antimicrobial Surface Protection

Logo, VS

Target Market(s)

Hospitals, Transport agencies, Airlines, Corporate entities

Contact Information for Business Card

Company name, VelaShield
Logo, VS

Gareth Tolley
velashieldnz@postbox.example
+64219305562
www.velashield.example.nz

Requirements
Must have
• Simple clean look.
Nice to have
• We apply nano coatings so try and incorporate this into a theme somehow

```html
<!DOCTYPE html>
<html lang="en">
<head>
<meta charset="utf-8">
<title>VelaShield Business Cards</title>
<link rel="stylesheet" href="https://fonts.googleapis.com/css2?family=Michroma&family=Montserrat:wght@400;500&display=swap">
<style>
  :root {
    --stage: #1c1c1c;
    --card-dark: #3e3e3e;
    --card-light: #ffffff;
    --ink-dark: #3a3a3a;
    --ink-light: #ffffff;
    --brand-blue: #4a97db;
    --rule: #4a4a4a;
    --sub-light: #e6e6e6;
    --sub-dark: #555555;
  }
  * { margin: 0; padding: 0; box-sizing: border-box; }
  html, body { width: 1200px; height: 900px; overflow: hidden; }
  body {
    background: var(--stage);
    position: relative;
    font-family: "Montserrat", sans-serif;
  }
  .card {
    position: absolute;
    left: 250px;
    width: 700px;
    height: 400px;
    box-shadow: 0 10px 30px rgba(0,0,0,0.5);
    overflow: hidden;
  }
  .card--front { top: 35px; background: var(--card-dark); }
  .card--back { top: 465px; background: var(--card-light); }

  .brand {
    position: absolute;
    left: 0; right: 0;
    display: flex;
    flex-direction: column;
    align-items: center;
  }
  .card--front .brand { top: 135px; }
  .card--back .brand { top: 45px; }

  .brand__row { display: flex; align-items: center; gap: 14px; }
  .brand__dot {
    width: 34px; height: 34px;
    border-radius: 50%;
    background: var(--brand-blue);
  }
  .brand__name {
    font-family: "Michroma", sans-serif;
    font-size: 46px;
    letter-spacing: 2px;
    text-transform: uppercase;
    line-height: 1;
  }
  .card--front .brand__name { color: var(--ink-light); }
  .card--back .brand__name { color: var(--ink-dark); font-size: 40px; }
  .brand__tagline {
    margin-top: 12px;
    font-size: 15px;
    letter-spacing: 1px;
    text-transform: uppercase;
  }
  .card--front .brand__tagline { color: var(--sub-light); }
  .card--back .brand__tagline { color: var(--sub-dark); font-size: 13px; }

  .divider {
    position: absolute;
    left: 70px; right: 70px; top: 185px;
    height: 2px;
    background: var(--rule);
  }
  .person-name {
    position: absolute;
    left: 70px; top: 225px;
    font-family: "Michroma", sans-serif;
    font-size: 28px;
    letter-spacing: 2px;
    color: var(--brand-blue);
    text-transform: uppercase;
  }
  .accent-bar {
    position: absolute;
    left: 40px; bottom: 0;
    width: 300px; height: 18px;
    background: var(--ink-dark);
  }
  .contacts {
    position: absolute;
    right: 60px; top: 262px;
    list-style: none;
  }
  .contacts__item {
    display: flex;
    justify-content: flex-end;
    align-items: center;
    gap: 12px;
    font-size: 20px;
    color: var(--ink-dark);
    line-height: 1.5;
  }
  .contacts__icon { width: 22px; height: 22px; flex: none; }
</style>
</head>
<body>
  <section class="card card--front">
    <div class="brand">
      <div class="brand__row">
        <span class="brand__dot"></span>
        <span class="brand__name">VelaShield</span>
      </div>
      <p class="brand__tagline">Antimicrobial Surface Protection</p>
    </div>
  </section>

  <section class="card card--back">
    <div class="brand">
      <div class="brand__row">
        <span class="brand__dot"></span>
        <span class="brand__name">VelaShield</span>
      </div>
      <p class="brand__tagline">Antimicrobial Surface Protection</p>
    </div>
    <div class="divider"></div>
    <h1 class="person-name">Gareth Tolley</h1>
    <ul class="contacts">
      <li class="contacts__item">+64219305562
        <svg class="contacts__icon" viewBox="0 0 24 24" fill="none" stroke="#4a97db" stroke-width="1.8" stroke-linecap="round" stroke-linejoin="round" aria-hidden="true">
          <path d="M5 3h4l2 5-2.5 1.5a11 11 0 0 0 6 6L16 13l5 2v4a2 2 0 0 1-2 2A17 17 0 0 1 3 5a2 2 0 0 1 2-2z"/>
        </svg>
      </li>
      <li class="contacts__item">velashieldnz@postbox.example
        <svg class="contacts__icon" viewBox="0 0 24 24" fill="none" stroke="#4a97db" stroke-width="1.8" stroke-linejoin="round" aria-hidden="true">
          <rect x="2" y="5" width="20" height="14" rx="1"/>
          <path d="M2 6l10 7 10-7"/>
        </svg>
      </li>
      <li class="contacts__item">www.velashield.example.nz
        <svg class="contacts__icon" viewBox="0 0 24 24" fill="none" stroke="#4a97db" stroke-width="1.8" aria-hidden="true">
          <circle cx="12" cy="12" r="10"/>
          <ellipse cx="12" cy="12" rx="4.5" ry="10"/>
          <path d="M2 12h20M4 7h16M4 17h16"/>
        </svg>
      </li>
    </ul>
    <div class="accent-bar"></div>
  </section>
</body>
</html>
```